Crestline Gas and Plumbing Business Card Design

I am after a business card design for my plumbing business called 'Crestline Gas & Plumbing'. I do all types of plumbing and gas work and specialise in general maintenance plumbing. Would like to see designs using current logo

Industry/Entity Type

Plumbing

Contact Information for Business Card

Name - Dale Whitcombe
Phone number - 0455163027
Email - admin@crestlinegasandplumbing.example.com.au
ABN - 68204915336

```html
<!DOCTYPE html>
<html lang="en">
<head>
<meta charset="utf-8">
<title>Crestline Gas &amp; Plumbing – Business Card</title>
<link rel="stylesheet" href="https://fonts.googleapis.com/css2?family=Poppins:wght@400;600;800&display=swap">
<style>
  :root {
    --stage: #04050f;
    --card-white: #ffffff;
    --brand-orange: #f7941d;
    --soft-orange: #fdc68b;
    --pill-grey: #e8e8ea;
    --ink: #2b3540;
    --ink-soft: #3a4049;
  }
  * { box-sizing: border-box; margin: 0; padding: 0; }
  html, body {
    width: 1200px; height: 900px; overflow: hidden;
    background: var(--stage);
    font-family: "Poppins", sans-serif;
  }
  .stage {
    width: 1200px; height: 900px;
    display: flex; flex-direction: column;
    align-items: center; justify-content: center; gap: 40px;
  }
  .card {
    position: relative;
    width: 640px; height: 366px;
    overflow: hidden;
  }

  /* Front */
  .card-front { background: var(--card-white); }
  .side-band {
    position: absolute; left: 0; top: 0; bottom: 0; width: 28px;
    background: var(--soft-orange);
  }
  .company-name {
    position: absolute; left: 74px; top: 78px;
    font-weight: 800; font-size: 26px; line-height: 1.05;
    color: var(--ink); text-transform: uppercase; letter-spacing: 0.5px;
  }
  .name-pill {
    position: absolute; left: 330px; top: 122px; right: -24px; height: 42px;
    background: var(--pill-grey); border-radius: 21px;
    display: flex; align-items: center; padding-left: 24px;
  }
  .name-pill .holder-name {
    font-weight: 600; font-size: 17px; color: var(--ink);
  }
  .pill-cap {
    position: absolute; right: -24px; top: 122px; width: 86px; height: 42px;
    background: var(--soft-orange); border-radius: 21px;
  }
  .contact-list {
    position: absolute; left: 90px; bottom: 40px;
    list-style: none; display: flex; flex-direction: column; gap: 6px;
  }
  .contact-list li {
    display: flex; align-items: center; gap: 10px;
    font-size: 13px; font-weight: 400; color: var(--ink-soft);
  }
  .contact-icon { width: 18px; height: 18px; flex: none; }

  /* Back */
  .card-back { background: var(--brand-orange); }
  .back-tab {
    position: absolute; left: -30px; bottom: 78px; width: 150px; height: 52px;
    background: var(--card-white); border-radius: 26px;
  }
  .back-brand {
    position: absolute; left: 0; right: 0; top: 0; bottom: 0;
    display: flex; align-items: center; justify-content: center; gap: 16px;
  }
  .back-brand .brand-dot {
    width: 54px; height: 54px; border-radius: 50%; background: var(--card-white);
  }
  .back-brand .brand-name {
    font-weight: 800; font-size: 34px; line-height: 1.05;
    color: var(--card-white); text-transform: uppercase; letter-spacing: 0.5px;
  }
</style>
</head>
<body>
<main class="stage">

  <section class="card card-front" aria-label="Business card front">
    <div class="side-band"></div>
    <div class="company-name">Crestline<br>Gas &amp; Plumbing</div>
    <div class="name-pill"><span class="holder-name">Dale Whitcombe</span></div>
    <div class="pill-cap"></div>
    <ul class="contact-list">
      <li>
        <svg class="contact-icon" viewBox="0 0 18 18" aria-hidden="true">
          <circle cx="9" cy="9" r="9" fill="#2b3540"/>
          <path d="M6 5.2c.4-.3.9-.2 1.1.2l.8 1.5c.2.4.1.8-.2 1l-.5.4c.4.9 1.1 1.6 2 2l.4-.5c.3-.3.7-.4 1-.2l1.5.8c.4.2.5.7.2 1.1l-.5.7c-.4.5-1.1.6-1.7.4-2.1-.8-3.7-2.4-4.5-4.5-.2-.6-.1-1.3.4-1.7z" fill="#fff"/>
        </svg>
        <span>0455163027</span>
      </li>
      <li>
        <svg class="contact-icon" viewBox="0 0 18 18" aria-hidden="true">
          <circle cx="9" cy="9" r="9" fill="#2b3540"/>
          <rect x="4.5" y="6" width="9" height="6.5" rx="1" fill="none" stroke="#fff" stroke-width="1.1"/>
          <circle cx="7" cy="8.6" r="1" fill="#fff"/>
          <path d="M9.5 8h2.5M9.5 10h2.5" stroke="#fff" stroke-width="1"/>
        </svg>
        <span>ABN - 68204915336</span>
      </li>
      <li>
        <svg class="contact-icon" viewBox="0 0 18 18" aria-hidden="true">
          <circle cx="9" cy="9" r="9" fill="#2b3540"/>
          <rect x="4.5" y="6" width="9" height="6.5" rx="0.8" fill="none" stroke="#fff" stroke-width="1.1"/>
          <path d="M4.8 6.4 9 9.6l4.2-3.2" fill="none" stroke="#fff" stroke-width="1.1"/>
        </svg>
        <span>admin@crestlinegasandplumbing.example.com.au</span>
      </li>
      <li>
        <svg class="contact-icon" viewBox="0 0 18 18" aria-hidden="true">
          <circle cx="9" cy="9" r="9" fill="#2b3540"/>
          <circle cx="9" cy="9" r="4.3" fill="none" stroke="#fff" stroke-width="1.1"/>
          <ellipse cx="9" cy="9" rx="1.8" ry="4.3" fill="none" stroke="#fff" stroke-width="1"/>
          <path d="M4.7 9h8.6" stroke="#fff" stroke-width="1"/>
        </svg>
        <span>www.crestlinegasandplumbing.example.com.au</span>
      </li>
    </ul>
  </section>

  <section class="card card-back" aria-label="Business card back">
    <div class="back-tab"></div>
    <div class="back-brand">
      <span class="brand-dot"></span>
      <span class="brand-name">Crestline<br>Gas &amp; Plumbing</span>
    </div>
  </section>

</main>
</body>
</html>
```